Awesome Business Card Design needed!

Hey there.
I'm looking for a simple but awesome business card design.
Type of company: Online advertisement agency
(please don't use the typical business people or statistics images on the card)
The front has to display the business name
and possibly some sort of logo ( perhaps something with the two M's of the biz name )
And the back of the card should say:
Name
Phone
Email
Let your imagination flow.
here are some designs that I like and that you can use as inspiration.
Simple but Awesome
http://images.pixelvantor.net/designs/55128_877673_43091_thumbnail.jpg
http://images.pixelvantor.net/designs/37714_747642_40106_image.jpg
http://images.pixelvantor.net/designs/55128_877673_43091_image.jpg
http://images.pixelvantor.net/designs/51321_781878_43091_image.jpg
http://images.pixelvantor.net/designs/33378_399063_15912_image.jpg
http://images.pixelvantor.net/designs/2337_271604_9495_image.jpg
good luck

```html
<!DOCTYPE html>
<html lang="en">
<head>
<meta charset="utf-8">
<title>Korvale Media — Business Card</title>
<link rel="stylesheet" href="https://fonts.googleapis.com/css2?family=Arimo:wght@700&display=swap">
<style>
  :root {
    --page: #ffffff;
    --stage-light: #a9a9a9;
    --stage-dark: #000000;
    --card-black: #000000;
    --card-black-glow: #262626;
    --card-red: #ff0000;
    --card-red-deep: #8a0000;
    --card-red-edge: #140000;
    --brand-orange: #ff6a00;
    --muted-text: #5b3b3b;
  }
  html, body {
    margin: 0;
    padding: 0;
    width: 1200px;
    height: 900px;
    overflow: hidden;
    background: var(--page);
    font-family: "Arimo", Arial, sans-serif;
    font-weight: 700;
  }
  .canvas {
    position: relative;
    width: 1200px;
    height: 900px;
  }
  .stage {
    position: absolute;
    left: 29px;
    top: 88px;
    width: 1150px;
    height: 491px;
    box-sizing: border-box;
    border: 1px solid #555;
    background: radial-gradient(ellipse 620px 360px at 570px 240px, var(--stage-light) 0%, #6a6a6a 45%, #262626 78%, var(--stage-dark) 100%);
  }
  .card {
    position: absolute;
    top: 170px;
    width: 481px;
    height: 275px;
    border-radius: 20px;
    overflow: hidden;
  }
  .card--front {
    left: 90px;
    background: radial-gradient(ellipse 260px 150px at 240px 130px, var(--card-black-glow) 0%, var(--card-black) 100%);
  }
  .card--back {
    left: 622px;
    background: radial-gradient(ellipse 330px 260px at 230px 100px, var(--card-red) 0%, #d00000 35%, var(--card-red-deep) 70%, var(--card-red-edge) 100%);
  }
  .brand {
    position: absolute;
    display: flex;
    align-items: center;
    gap: 10px;
    color: var(--brand-orange);
    font-size: 30px;
    letter-spacing: 0.5px;
    white-space: nowrap;
  }
  .brand__mark {
    width: 22px;
    height: 22px;
    background: var(--brand-orange);
  }
  .card--front .brand {
    left: 50%;
    top: 118px;
    transform: translateX(-50%);
  }
  .card--back .brand {
    right: 26px;
    top: 58px;
  }
  .contact {
    position: absolute;
    right: 306px;
    top: 186px;
    text-align: right;
    font-size: 14px;
    line-height: 17px;
    color: var(--muted-text);
  }
  .contact__lead {
    color: var(--brand-orange);
  }
</style>
</head>
<body>
  <main class="canvas">
    <div class="stage"></div>

    <section class="card card--front" aria-label="Card front">
      <div class="brand">
        <span class="brand__mark"></span>
        <span class="brand__name">KORVALE MEDIA</span>
      </div>
    </section>

    <section class="card card--back" aria-label="Card back">
      <div class="brand">
        <span class="brand__mark"></span>
        <span class="brand__name">KORVALE MEDIA</span>
      </div>
      <div class="contact">
        <div class="contact__line"><span class="contact__lead">MILO</span> SANTOS</div>
        <div class="contact__line"><span class="contact__lead">555</span> 010 4821</div>
        <div class="contact__line"><span class="contact__lead">hi</span> @korvale.net</div>
      </div>
    </section>
  </main>
</body>
</html>
```